Young and modern Electrical company working in the commercial arena.

Wanting a business card design thats modern and will last. Maybe Minimalist? Happy to look at changing my logo

Target Market(s)

Builders, Project Managers

Industry/Entity Type

Electrical

Contact Information for Business Card

Name
Address
Phone number
Job title

Logo Text

our name or just the logo i'm open to ideas

Font styles to use
Sans Serif

Requirements
Nice to have
• would like to keep the purple in our current logo. it's kinda unique to our market
Should not have
• Don't want it to be to busy. simple is best i think

```html
<!DOCTYPE html>
<html lang="en">
<head>
<meta charset="utf-8">
<title>Voltline Electrical – Business Card</title>
<link rel="stylesheet" href="https://fonts.googleapis.com/css2?family=Open+Sans:wght@400;600;700&display=swap">
<style>
  :root {
    --bg: #26282c;
    --purple: #6a3fa3;
    --purple-deep: #5b3593;
    --white: #ffffff;
    --card-w: 560px;
    --card-h: 320px;
  }
  * { margin: 0; padding: 0; box-sizing: border-box; }
  html, body {
    width: 1200px; height: 900px; overflow: hidden;
    background: var(--bg);
    font-family: "Open Sans", sans-serif;
  }
  .canvas {
    position: relative; width: 1200px; height: 900px;
  }
  .card {
    position: absolute;
    width: var(--card-w); height: var(--card-h);
    border-radius: 26px; overflow: hidden;
    background: var(--white);
    box-shadow: 0 14px 30px rgba(0,0,0,.35);
  }
  .card-front { left: 320px; top: 100px; }
  .card-back  { left: 320px; top: 480px; }
  .card-shapes { position: absolute; inset: 0; width: 100%; height: 100%; }

  .brand {
    position: absolute;
    display: flex; align-items: center; gap: 10px;
    color: var(--purple);
    font-weight: 600; font-size: 26px; letter-spacing: .5px;
    white-space: nowrap;
  }
  .brand-dot {
    width: 16px; height: 16px; border-radius: 50%;
    background: var(--purple);
  }
  .card-front .brand { left: 40px; top: 52px; }
  .card-back .brand { left: 50%; top: 50%; transform: translate(-50%, -50%); }

  .contact {
    position: absolute; left: 290px; top: 150px;
    color: var(--white);
  }
  .contact-name {
    font-weight: 700; font-size: 22px; letter-spacing: 1px; line-height: 1.1;
  }
  .contact-role {
    font-weight: 600; font-size: 12px; letter-spacing: 1px;
    padding-bottom: 6px; margin-bottom: 12px;
    border-bottom: 1.5px solid var(--white);
    width: 230px;
  }
  .contact-list { list-style: none; }
  .contact-item {
    display: flex; align-items: center; gap: 9px;
    font-size: 12.5px; margin-bottom: 8px;
  }
  .contact-icon {
    width: 20px; height: 20px; border-radius: 50%;
    background: var(--white);
    display: flex; align-items: center; justify-content: center;
    flex: none;
  }
  .contact-icon svg { width: 12px; height: 12px; }
</style>
</head>
<body>
<main class="canvas">

  <section class="card card-front" aria-label="Business card front">
    <svg class="card-shapes" viewBox="0 0 560 320" preserveAspectRatio="none" aria-hidden="true">
      <defs>
        <linearGradient id="frontPurple" x1="0" y1="0" x2="1" y2="1">
          <stop offset="0" stop-color="#7248ad"/>
          <stop offset="1" stop-color="#5b3593"/>
        </linearGradient>
      </defs>
      <polygon points="0,130 560,60 560,320 0,320" fill="url(#frontPurple)"/>
    </svg>
    <div class="brand"><span class="brand-dot"></span>Voltline Electrical</div>
    <div class="contact">
      <p class="contact-name">MARCUS BELL</p>
      <p class="contact-role">DOCTOR</p>
      <ul class="contact-list">
        <li class="contact-item">
          <span class="contact-icon">
            <svg viewBox="0 0 24 24"><path fill="#6a3fa3" d="M6.6 10.8a15 15 0 0 0 6.6 6.6l2.2-2.2a1 1 0 0 1 1-.25 11 11 0 0 0 3.6.6 1 1 0 0 1 1 1V20a1 1 0 0 1-1 1A17 17 0 0 1 3 4a1 1 0 0 1 1-1h3.5a1 1 0 0 1 1 1c0 1.25.2 2.45.6 3.6a1 1 0 0 1-.25 1z"/></svg>
          </span>03 5550 1820
        </li>
        <li class="contact-item">
          <span class="contact-icon">
            <svg viewBox="0 0 24 24"><rect x="3" y="6" width="18" height="12" fill="none" stroke="#6a3fa3" stroke-width="2"/><path d="M3 6l9 7 9-7" fill="none" stroke="#6a3fa3" stroke-width="2"/></svg>
          </span>hello@voltlinecommercial.com.au
        </li>
        <li class="contact-item">
          <span class="contact-icon">
            <svg viewBox="0 0 24 24"><circle cx="12" cy="12" r="9" fill="none" stroke="#6a3fa3" stroke-width="2"/><path d="M3 12h18M12 3c3 3 3 15 0 18M12 3c-3 3-3 15 0 18" fill="none" stroke="#6a3fa3" stroke-width="1.6"/></svg>
          </span>www.voltlinecommercial.com.au
        </li>
      </ul>
    </div>
  </section>

  <section class="card card-back" aria-label="Business card back">
    <svg class="card-shapes" viewBox="0 0 560 320" preserveAspectRatio="none" aria-hidden="true">
      <defs>
        <linearGradient id="backPurple" x1="0" y1="0" x2="1" y2="1">
          <stop offset="0" stop-color="#7248ad"/>
          <stop offset="1" stop-color="#5b3593"/>
        </linearGradient>
      </defs>
      <polygon points="0,0 560,0 560,40 0,110" fill="var(--purple-deep)"/>
      <polygon points="0,270 560,200 560,320 0,320" fill="url(#backPurple)"/>
    </svg>
    <div class="brand"><span class="brand-dot"></span>Voltline Electrical</div>
  </section>

</main>
</body>
</html>
```